Design Creative Banner or Gif Ads. 3 Designs To Be Selected

Come up with some creative banner ads for crestline.co.nz

*At least 3 different winning banners will be chosen*

Please provide banner ads / gif ads in common google ads / website banner formats.

They can be gif or static but must stand out while still maintaining clear clean text and visuals, with a premium professional feel (please avoid clip art or anything that gives a cheap message).

Please keep in mind that these will likely be small ads so text needs to be large and if there's there a lot of text then use multiple frames/ pages as submit as a gif.

Style
Minimal & clean lines
Architectural or realistic images
Avoid cartoon styles, clipart, or anything that looks cheap

Font
Nexa or Montserrat or similar

Tone
Premium, serious, trustworthy — fits new builds

Colours
Option 1: Deep Navy (trust & quality) & lighter blues and warm grey
Option 2: Open to bright colours to help the ads stand out, such as (but not limited to) bright pink with black, yellow, fluorescent green, provided the messaging is still done professionally.
Our logo is attached (Crest Line Logo)

Display Sizes
Ad specs for file sizes should be file formats like JPEG, GIF, and PNG, with animations limited to a max of 30 seconds or less.
We will need several different ad sizes provided for each of the 3 selected winning designs.

• Medium Rectangle: 300 × 250 pixels
• Leaderboard: 728 × 90 pixels
• Desktop Banner ad image: (640x360 pixels)
• Desktop Banner ad image 2: (300x600 pixels)
• Possibly one or two other sizes

Flexibility to be creative
The ad text, words, upper/lower case, layout, colour, theme, and images can be adjusted to how you think it will look best. The follow example ads are just examples of what we are after but we are keen to see what you can create.

Recommendations at this point:
1. Avoid text heavy
2. Looking for more Gif ads
3. Imaging: if possible use real stock photo's rather than AI

Themes:

1
Building Soon? Start Here
Free Build Planning Pack:
✓ Build Cost Calculator
✓ Hidden Cost Checklist
✓ Builder Comparison Guide
Build With Confidence
Download Free

2
Before You Choose A Builder
Compare Price, Scope, Risk & Value
Avoid Costly Mistakes
Choose The Right Builder With Confidence
Download The Free Guide

3
Planning A New Build?
Avoid These Common Mistakes:
✗ Hidden Exclusions
✗ Missing Scope
✗ Unrealistic Allowances
✗ Budget Blowouts
Download The Free Guide

4
Before You Buy Land
Know what it could cost to build.
Avoid Costly Building Mistakes
Download Our Free Guides

5
Know Your Build Budget?
• Free Build Cost Calculator
• Hidden Cost Checklist
• Build Planning Tools
Calculate Costs (Download)

Target Market(s)

Landowners looking to build

Industry/Entity Type

Building

Font styles to use
Other font styles liked:
• Nexa or Montserrat or similar

Requirements
Should not have
• Avoid cartoon styles, clipart, or anything that looks cheap

```html
<!DOCTYPE html>
<html lang="en">
<head>
<meta charset="utf-8">
<title>Crest Line Banner Set</title>
<link href="https://fonts.googleapis.com/css2?family=Montserrat:wght@400;500;600;700&display=swap" rel="stylesheet">
<style>
:root{
  --page:#e6e7e9;
  --navy:#10304d;
  --navy-deep:#0b2238;
  --accent:#2a9fd6;
  --title:#2b9fd4;
  --white:#ffffff;
  --label:#1d1d1d;
}
*{box-sizing:border-box;margin:0;padding:0}
html,body{width:1200px;height:952px;overflow:hidden;background:var(--page);font-family:'Montserrat',sans-serif}
.sheet{position:relative;width:1200px;height:952px}
.size-label{position:absolute;font-size:16px;color:var(--label);font-family:'Montserrat',sans-serif;line-height:1}
.ad{position:absolute;overflow:hidden;color:var(--white);
  background:linear-gradient(115deg,var(--navy-deep) 0%,var(--navy) 45%,#123756 70%,var(--navy-deep) 100%);
  border-bottom:4px solid var(--accent)}
.ad > *{position:absolute}
.ad-title{color:var(--title);font-weight:700;line-height:1.05;white-space:nowrap}
.ad-sub{font-weight:400;line-height:1.2}
.ad-points{list-style:none}
.ad-points li{display:flex;align-items:center;line-height:1.15}
.ad-points svg{flex:none;fill:none;stroke:var(--accent);stroke-width:1.6}
.brand{display:flex;flex-direction:column}
.brand-row{display:flex;align-items:center}
.brand-mark{background:var(--white);flex:none}
.brand-name{font-weight:700;white-space:nowrap;line-height:1}
.brand-tag{font-size:3px;letter-spacing:.2px;text-transform:uppercase;opacity:.8;white-space:nowrap;margin-top:2px}
.guide{font-weight:500;white-space:nowrap}
.cta{border:1.5px solid var(--white);border-radius:4px;background:#1a6a9a;display:flex;align-items:center;justify-content:center;white-space:nowrap;font-weight:500}
.photo{background:linear-gradient(135deg,rgba(16,48,77,0) 0%,#9a8a70 30%,#d8d5cf 55%,#f1f1ef 75%,#8c939a 100%);
  -webkit-mask-image:linear-gradient(90deg,transparent 0%,#000 25%);mask-image:linear-gradient(90deg,transparent 0%,#000 25%)}

/* Leaderboard 728x90 */
.ad--leader{left:59px;top:73px;width:1055px;height:130px}
.ad--leader .ad-title{left:30px;top:28px;font-size:38px}
.ad--leader .ad-sub{left:30px;top:69px;font-size:17px}
.ad--leader .ad-points{left:332px;top:30px;font-size:17px}
.ad--leader .ad-points li{height:25px;gap:10px}
.ad--leader .brand{left:583px;top:28px}
.ad--leader .brand-mark{width:30px;height:22px;margin-right:10px}
.ad--leader .brand-name{font-size:16px}
.ad--leader .brand-tag{margin-left:40px}
.ad--leader .guide{left:593px;top:70px;font-size:10px}
.ad--leader .cta{left:600px;top:82px;width:113px;height:23px;font-size:11.5px}
.ad--leader .photo{left:790px;top:0;width:265px;height:126px}

/* Medium rectangle 300x250 */
.ad--rect{left:59px;top:239px;width:435px;height:362px}
.ad--rect .brand{left:31px;top:27px}
.ad--rect .brand-mark{width:32px;height:24px;margin-right:10px}
.ad--rect .brand-name{font-size:16px}
.ad--rect .brand-tag{margin-left:42px}
.ad--rect .ad-title{left:33px;top:70px;font-size:38px}
.ad--rect .ad-sub{left:33px;top:121px;font-size:16.5px}
.ad--rect .ad-points{left:37px;top:172px;font-size:17px}
.ad--rect .ad-points li{height:25px;gap:12px}
.ad--rect .guide{left:43px;top:271px;font-size:11.5px}
.ad--rect .cta{left:50px;top:291px;width:133px;height:27px;font-size:13px}
.ad--rect .photo{left:229px;top:170px;width:206px;height:188px}

/* 300x90 */
.ad--strip{left:511px;top:239px;width:435px;height:130px}
.ad--strip .ad-title{left:20px;top:14px;font-size:23px}
.ad--strip .ad-sub{left:20px;top:45px;font-size:11px}
.ad--strip .ad-points{left:21px;top:73px;font-size:11px}
.ad--strip .ad-points li{height:16px;gap:7px}
.ad--strip .brand{left:172px;top:66px}
.ad--strip .brand-mark{width:18px;height:13px;margin-right:6px}
.ad--strip .brand-name{font-size:10px}
.ad--strip .brand-tag{font-size:2.5px;margin-left:24px}
.ad--strip .guide{left:180px;top:90px;font-size:5.5px}
.ad--strip .cta{left:183px;top:101px;width:62px;height:12px;font-size:6px;border-width:1px;border-radius:2px}
.ad--strip .photo{left:255px;top:0;width:180px;height:126px}

/* 90x160 */
.ad--mini{left:812px;top:398px;width:130px;height:232px}
.ad--mini .brand{left:16px;top:13px}
.ad--mini .brand-mark{width:19px;height:14px;margin-right:7px}
.ad--mini .brand-name{font-size:10px}
.ad--mini .brand-tag{font-size:2.5px;margin-left:26px}
.ad--mini .ad-title{left:16px;top:42px;font-size:18px;white-space:normal}
.ad--mini .ad-sub{left:16px;top:88px;font-size:8.5px;line-height:1.7}
.ad--mini .ad-points{left:16px;top:125px;font-size:7px}
.ad--mini .ad-points li{height:12px;gap:4px}
.ad--mini .guide{left:30px;top:170px;font-size:5.5px}
.ad--mini .cta{left:35px;top:181px;width:61px;height:11px;font-size:5.5px;border-width:1px;border-radius:2px;z-index:2}
.ad--mini .photo{left:0;top:186px;width:130px;height:42px;-webkit-mask-image:linear-gradient(180deg,transparent 0%,#000 40%);mask-image:linear-gradient(180deg,transparent 0%,#000 40%)}

/* 160x600 */
.ad--sky{left:964px;top:239px;width:178px;height:670px}
.ad--sky .brand{left:24px;top:22px}
.ad--sky .brand-mark{width:28px;height:21px;margin-right:9px}
.ad--sky .brand-name{font-size:14px}
.ad--sky .brand-tag{font-size:2.5px;margin-left:37px}
.ad--sky .ad-title{left:22px;top:78px;font-size:29px;white-space:normal;line-height:1.2}
.ad--sky .ad-sub{left:22px;top:157px;font-size:14px;line-height:1.25}
.ad--sky .ad-points{left:24px;top:226px;font-size:13px}
.ad--sky .ad-points li{height:46px;gap:10px;align-items:flex-start}
.ad--sky .ad-points svg{margin-top:2px}
.ad--sky .guide{left:37px;top:384px;font-size:8.5px}
.ad--sky .cta{left:43px;top:399px;width:96px;height:20px;font-size:9.5px}
.ad--sky .photo{left:0;top:457px;width:178px;height:209px;-webkit-mask-image:linear-gradient(180deg,transparent 0%,#000 25%);mask-image:linear-gradient(180deg,transparent 0%,#000 25%)}

/* 480x80 */
.ad--wide{left:59px;top:658px;width:695px;height:115px}
.ad--wide .ad-title{left:20px;top:20px;font-size:27px}
.ad--wide .ad-sub{left:20px;top:55px;font-size:13px}
.ad--wide .ad-points{left:245px;top:27px;font-size:14px}
.ad--wide .ad-points li{height:21px;gap:9px}
.ad--wide .brand{left:442px;top:26px}
.ad--wide .brand-mark{width:24px;height:18px;margin-right:8px}
.ad--wide .brand-name{font-size:13px}
.ad--wide .brand-tag{font-size:2.5px;margin-left:32px}
.ad--wide .guide{left:438px;top:53px;font-size:8.5px}
.ad--wide .cta{left:444px;top:69px;width:96px;height:19px;font-size:9.5px}
.ad--wide .photo{left:545px;top:0;width:150px;height:111px}

/* 480x60 */
.ad--slim{left:59px;top:817px;width:695px;height:87px}
.ad--slim .ad-title{left:20px;top:15px;font-size:23px}
.ad--slim .ad-sub{left:20px;top:45px;font-size:11px;line-height:1.15}
.ad--slim .ad-points{left:225px;top:17px;font-size:13.5px}
.ad--slim .ad-points li{height:21px;gap:8px}
.ad--slim .brand{left:427px;top:16px}
.ad--slim .brand-mark{width:20px;height:15px;margin-right:7px}
.ad--slim .brand-name{font-size:11px}
.ad--slim .brand-tag{font-size:2.5px;margin-left:27px}
.ad--slim .guide{left:425px;top:41px;font-size:7px}
.ad--slim .cta{left:430px;top:54px;width:84px;height:16px;font-size:8px}
.ad--slim .photo{left:550px;top:0;width:145px;height:83px}
</style>
</head>
<body>
<svg width="0" height="0" style="position:absolute" aria-hidden="true">
  <symbol id="icon-warning" viewBox="0 0 16 16"><path d="M8 2 L15 14 H1 Z"/><path d="M8 6.5v4M8 12v.6"/></symbol>
  <symbol id="icon-budget" viewBox="0 0 16 16"><rect x="2" y="1.5" width="9" height="12"/><rect x="5" y="4" width="9" height="11"/><path d="M7 7h5M7 9.5h5M7 12h3"/></symbol>
  <symbol id="icon-contract" viewBox="0 0 16 16"><path d="M10 2H2v12h9"/><path d="M4 5h4M4 8h3"/><path d="M8 12l1-3 5-5 2 2-5 5z"/></symbol>
</svg>

<main class="sheet">

  <span class="size-label" style="left:59px;top:47px">728X90px</span>
  <section class="ad ad--leader">
    <h2 class="ad-title">Bought Land?</h2>
    <p class="ad-sub">Before You Choose A Builder,<br>Read This.</p>
    <ul class="ad-points">
      <li><svg width="18" height="18"><use href="#icon-warning"/></svg>Avoid Costly Mistakes</li>
      <li><svg width="18" height="18"><use href="#icon-budget"/></svg>Budget Blowouts</li>
      <li><svg width="18" height="18"><use href="#icon-contract"/></svg>Contract Surprises</li>
    </ul>
    <div class="brand"><div class="brand-row"><span class="brand-mark"></span><span class="brand-name">Crest Line</span></div><span class="brand-tag">Compare quotes from trusted builders</span></div>
    <p class="guide">Free Build Planning Guide</p>
    <span class="cta">Download Now!</span>
    <div class="photo" role="img" aria-label="Photo of a timber-framed house under construction with scaffolding"></div>
  </section>

  <section class="ad ad--rect">
    <div class="brand"><div class="brand-row"><span class="brand-mark"></span><span class="brand-name">Crest Line</span></div><span class="brand-tag">Compare quotes from trusted builders</span></div>
    <h2 class="ad-title">Bought Land?</h2>
    <p class="ad-sub">Before You Choose A Builder, Read This.</p>
    <ul class="ad-points">
      <li><svg width="18" height="18"><use href="#icon-warning"/></svg>Avoid Costly Mistakes</li>
      <li><svg width="18" height="18"><use href="#icon-budget"/></svg>Budget Blowouts</li>
      <li><svg width="18" height="18"><use href="#icon-contract"/></svg>Contract Surprises</li>
    </ul>
    <div class="photo" role="img" aria-label="Photo of a timber-framed house under construction with scaffolding"></div>
    <p class="guide">Free Build Planning Guide</p>
    <span class="cta">Download Now!</span>
  </section>
  <span class="size-label" style="left:411px;top:609px">300X250px</span>

  <section class="ad ad--strip">
    <h2 class="ad-title">Bought Land?</h2>
    <p class="ad-sub">Before You Choose A Builder, Read This.</p>
    <ul class="ad-points">
      <li><svg width="12" height="12"><use href="#icon-warning"/></svg>Avoid Costly Mistakes</li>
      <li><svg width="12" height="12"><use href="#icon-budget"/></svg>Budget Blowouts</li>
      <li><svg width="12" height="12"><use href="#icon-contract"/></svg>Contract Surprises</li>
    </ul>
    <div class="photo" role="img" aria-label="Photo of a timber-framed house under construction with scaffolding"></div>
    <div class="brand"><div class="brand-row"><span class="brand-mark"></span><span class="brand-name">Crest Line</span></div><span class="brand-tag">Compare quotes from trusted builders</span></div>
    <p class="guide">Free Build Planning Guide</p>
    <span class="cta">Download Now!</span>
  </section>
  <span class="size-label" style="left:512px;top:375px">300X90px</span>

  <span class="size-label" style="left:1079px;top:220px">160x600</span>
  <section class="ad ad--sky">
    <div class="brand"><div class="brand-row"><span class="brand-mark"></span><span class="brand-name">Crest Line</span></div><span class="brand-tag">Compare quotes from trusted builders</span></div>
    <h2 class="ad-title">Bought<br>Land?</h2>
    <p class="ad-sub">Before You<br>Choose A Builder,<br>Read This.</p>
    <ul class="ad-points">
      <li><svg width="16" height="16"><use href="#icon-warning"/></svg>Avoid Costly<br>Mistakes</li>
      <li><svg width="16" height="16"><use href="#icon-budget"/></svg>Budget<br>Blowouts</li>
      <li><svg width="16" height="16"><use href="#icon-contract"/></svg>Contract<br>Surprises</li>
    </ul>
    <p class="guide">Free Build Planning Guide</p>
    <span class="cta">Download Now!</span>
    <div class="photo" role="img" aria-label="Photo of a timber-framed house under construction with scaffolding"></div>
  </section>

  <section class="ad ad--mini">
    <div class="brand"><div class="brand-row"><span class="brand-mark"></span><span class="brand-name">Crest Line</span></div><span class="brand-tag">Compare quotes from trusted builders</span></div>
    <h2 class="ad-title">Bought<br>Land?</h2>
    <p class="ad-sub" style="line-height:1.6">Before You Choose<br>A Builder, Read This.</p>
    <ul class="ad-points">
      <li><svg width="8" height="8"><use href="#icon-warning"/></svg>Avoid Costly Mistakes</li>
      <li><svg width="8" height="8"><use href="#icon-budget"/></svg>Budget Blowouts</li>
      <li><svg width="8" height="8"><use href="#icon-contract"/></svg>Contract Surprises</li>
    </ul>
    <p class="guide">Free Build Planning Guide</p>
    <div class="photo" role="img" aria-label="Photo of a timber-framed house under construction with scaffolding"></div>
    <span class="cta">Download Now!</span>
  </section>
  <span class="size-label" style="left:812px;top:634px">90X160px</span>

  <span class="size-label" style="left:59px;top:634px">480X80px</span>
  <section class="ad ad--wide">
    <h2 class="ad-title">Bought Land?</h2>
    <p class="ad-sub">Before You Choose A Builder,<br>Read This.</p>
    <ul class="ad-points">
      <li><svg width="15" height="15"><use href="#icon-warning"/></svg>Avoid Costly Mistakes</li>
      <li><svg width="15" height="15"><use href="#icon-budget"/></svg>Budget Blowouts</li>
      <li><svg width="15" height="15"><use href="#icon-contract"/></svg>Contract Surprises</li>
    </ul>
    <div class="photo" role="img" aria-label="Photo of a timber-framed house under construction with scaffolding"></div>
    <div class="brand"><div class="brand-row"><span class="brand-mark"></span><span class="brand-name">Crest Line</span></div></div>
    <p class="guide">Free Build Planning Guide</p>
    <span class="cta">Download Now!</span>
  </section>

  <span class="size-label" style="left:682px;top:795px">480X60px</span>
  <section class="ad ad--slim">
    <h2 class="ad-title">Bought Land?</h2>
    <p class="ad-sub">Before You Choose A Builder,<br>Read This.</p>
    <ul class="ad-points">
      <li><svg width="14" height="14"><use href="#icon-warning"/></svg>Avoid Costly Mistakes</li>
      <li><svg width="14" height="14"><use href="#icon-budget"/></svg>Budget Blowouts</li>
      <li><svg width="14" height="14"><use href="#icon-contract"/></svg>Contract Surprises</li>
    </ul>
    <div class="photo" role="img" aria-label="Photo of a timber-framed house under construction with scaffolding"></div>
    <div class="brand"><div class="brand-row"><span class="brand-mark"></span><span class="brand-name">Crest Line</span></div><span class="brand-tag">Compare quotes from trusted builders</span></div>
    <p class="guide">Free Build Planning Guide</p>
    <span class="cta">Download Now!</span>
  </section>

</main>
</body>
</html>
```